依頼詳細
今年の仮チラシをファイル添付しておきますので、講師の肩書、名前等の確認をお願いいたします。

昨年の講演会のチラシもファイル添付しておきますので、参考にお願いいたします。

こどもさんの笑顔の写真や、家族で幸せそうにしている写真がありそうでしたら、多めに使用していただけますか。
記載項目
記載項目は基本2018年のチラシと同じですので、ファイル添付分で確認をおねがいします。(日付だけが、9月21日(土)となります。)
サイズ
A4
ページ数
片面
希望イメージ
シンプル 複雑
単色 カラフル
暗い 明るい
日常 高級
遊び心 厳粛
未来的 伝統的
女性的 男性的
希望する色
水色系、緑系、黄・オレンジ系
納品ファイル
• 高解像度JPG (.jpg)
補足説明
今年の講演会チラシにも講師二人の写真を入れる予定です。撮影できしだいファイルをおくるかたちとなります。よろしくお願いいたします。
■ 選んだ理由

イメージと合ったから。

■ 提案者全員のお礼・コメント

みなさん、ご協力ありがとうございました。

```html
<!DOCTYPE html>
<html lang="ja">
<head>
<meta charset="utf-8">
<title>特別講演会 こどもの栄養×こどもの姿勢</title>
<link href="https://fonts.googleapis.com/css2?family=M+PLUS+Rounded+1c:wght@500;700;800&family=Noto+Sans+JP:wght@400;500;700&display=swap" rel="stylesheet">
<style>
:root{
  --green:#5aa83a;
  --green-dark:#3f8a2a;
  --orange:#f2921c;
  --leaf:#e6f2d6;
  --ink:#333;
  --paper:#ffffff;
}
*{margin:0;padding:0;box-sizing:border-box}
html,body{width:846px;height:1200px;overflow:hidden;background:var(--paper)}
body{font-family:"Noto Sans JP",sans-serif;color:var(--ink)}
.flyer{position:relative;width:846px;height:1200px;overflow:hidden;background:var(--paper)}
.hero-photo{position:absolute;left:250px;top:0;width:596px;height:530px;
  background:radial-gradient(ellipse at 60% 40%,#fff8e8 0%,#f1e6c8 35%,#cfe3b8 70%,#b8d79a 100%)}
.hero-fade{position:absolute;left:250px;top:0;width:200px;height:530px;
  background:linear-gradient(90deg,#fff 0%,rgba(255,255,255,0) 100%)}
.tag-event{position:absolute;left:60px;top:22px;width:220px;height:48px;background:var(--green);
  color:#fff;font:800 30px "M PLUS Rounded 1c",sans-serif;display:flex;align-items:center;justify-content:center;
  letter-spacing:.08em;border-radius:4px}
.subtitle{position:absolute;left:46px;top:78px;font:700 21px "M PLUS Rounded 1c",sans-serif;color:var(--green-dark)}
.topic{position:absolute;width:250px;height:250px;border-radius:50%;color:#fff;
  display:flex;flex-direction:column;align-items:center;justify-content:center;
  font-family:"M PLUS Rounded 1c",sans-serif;opacity:.94}
.topic small{font-size:34px;font-weight:700;line-height:1.1}
.topic strong{font-size:70px;font-weight:800;line-height:1.15}
.topic-nutrition{left:28px;top:190px;background:var(--orange)}
.topic-posture{left:228px;top:176px;background:var(--green)}
.cross{position:absolute;left:236px;top:290px;font:800 46px/1 "M PLUS Rounded 1c",sans-serif;color:#fff;z-index:2}
.kids{position:absolute;border-radius:50%}
.kids-a{left:20px;top:440px;width:200px;height:200px;background:radial-gradient(circle,#bfe3f5,#7cc3e6)}
.kids-b{left:150px;top:580px;width:170px;height:170px;background:radial-gradient(circle,#dff0c8,#9fcf74)}
.kids-c{left:30px;top:662px;width:190px;height:190px;background:radial-gradient(circle,#fde3c0,#f5b86a)}
.intro{position:absolute;left:340px;top:548px;width:480px;font-size:15px;line-height:1.7}
.label{display:inline-block;background:var(--green);color:#fff;font:700 16px "M PLUS Rounded 1c",sans-serif;padding:3px 14px;border-radius:3px}
.lecturers-label{position:absolute;left:340px;top:652px}
.lecturer{position:absolute;top:690px;width:240px}
.lecturer-1{left:340px}.lecturer-2{left:590px}
.lecturer .role{font-size:12px}
.lecturer .name{font:700 22px "Noto Sans JP",sans-serif}
.lecturer .name span{font-size:14px;font-weight:500}
.lecturer .portrait{position:absolute;right:10px;top:-4px;width:64px;height:64px;border-radius:50%;background:linear-gradient(#e8e1d4,#b9ad9a)}
.lecturer p{margin-top:16px;font-size:12px;line-height:1.65;width:230px}
.date-block{position:absolute;left:40px;top:872px;color:var(--green-dark)}
.era{font:700 18px "M PLUS Rounded 1c",sans-serif;color:var(--orange)}
.date{font:800 68px/1 "M PLUS Rounded 1c",sans-serif;white-space:nowrap}
.date .day{display:inline-flex;width:42px;height:42px;border-radius:50%;background:var(--green);color:#fff;font-size:24px;align-items:center;justify-content:center;vertical-align:middle;margin-left:4px}
.times{position:absolute;left:350px;top:908px;font:700 17px "Noto Sans JP",sans-serif;line-height:1.5;color:var(--ink);white-space:nowrap}
.fee{position:absolute;left:40px;top:972px;display:flex;align-items:center;gap:16px}
.fee .amount{font:800 32px "M PLUS Rounded 1c",sans-serif}
.fee .amount span{font-size:18px}
.fee-note{position:absolute;left:40px;top:1016px;font-size:11px}
.host{position:absolute;left:40px;top:1036px}
.host .org{font:700 21px/1.3 "Noto Sans JP",sans-serif;margin-top:4px}
.host .addr{font-size:11px;margin-top:2px;white-space:nowrap}
.venue{position:absolute;left:500px;top:890px;width:315px}
.venue-head{background:var(--green);color:#fff;font:700 18px "M PLUS Rounded 1c",sans-serif;padding:4px 14px}
.venue-name{font:700 24px "Noto Sans JP",sans-serif;margin-top:6px}
.venue-name span{font-size:13px}
.venue-addr{font-size:11px;margin-top:2px}
.venue-map{margin-top:8px;width:315px;height:120px;background:linear-gradient(135deg,#f3f3ee,#e0e6da);border:1px solid #ccc}
.contact{position:absolute;left:0;top:1140px;width:846px;height:44px;background:var(--leaf);display:flex;align-items:center;padding-left:40px;gap:20px;font-size:14px}
.contact .label{font-size:14px}
</style>
</head>
<body>
<main class="flyer">
  <div class="hero-photo" role="img" aria-label="母親が笑顔のこどもを抱き上げる明るい屋外の写真"></div>
  <div class="hero-fade"></div>

  <div class="tag-event">特別講演会</div>
  <p class="subtitle">こども達の輝かしい未来のために!!</p>

  <div class="topic topic-nutrition"><small>こどもの</small><strong>栄養</strong></div>
  <div class="topic topic-posture"><small>こどもの</small><strong>姿勢</strong></div>
  <div class="cross">×</div>

  <div class="kids kids-a" role="img" aria-label="青空の下で遊ぶこどもたちの写真"></div>
  <div class="kids kids-b" role="img" aria-label="芝生で笑う親子の写真"></div>
  <div class="kids kids-c" role="img" aria-label="笑顔のこどもの写真"></div>

  <p class="intro">平成17年に食育基本法が制定されて以来、長年学校教育で児童の栄養指導を行ってきたこどもの栄養専門家と大学で姿勢科学を修め、姿勢の専門家を数多く育ててきた博士&lt;健康科学&gt;によるコラボレーション講演会。</p>

  <div class="lecturers-label"><span class="label">講師紹介</span></div>

  <section class="lecturer lecturer-1">
    <div class="role">管理栄養士</div>
    <div class="name">森川 理沙 <span>氏</span></div>
    <div class="portrait" role="img" aria-label="講師の写真"></div>
    <p>【講演内容】アレルギーのこどもも安心して食べられる食事と、成長期に必要な栄養素、毎日の献立づくりのコツを分かりやすくお話しします。</p>
  </section>
  <section class="lecturer lecturer-2">
    <div class="role">博士（健康科学）</div>
    <div class="name">井上 隆之 <span>氏</span></div>
    <div class="portrait" role="img" aria-label="講師の写真"></div>
    <p>【講演内容】こどもの姿勢の乱れはなぜ起こるのか。正しい姿勢が学習や運動に与える良い影響と、家庭でできる簡単な姿勢づくりを紹介します。</p>
  </section>

  <div class="date-block">
    <div class="era">令和元年</div>
    <div class="date">9月21日<span class="day">土</span></div>
  </div>
  <div class="times">開演 13:30<br>開場 13:00～</div>

  <div class="fee"><span class="label">参加費</span><span class="amount">4,000<span>円</span></span></div>
  <p class="fee-note">※参加申込されたチケットをお持ちください。</p>

  <div class="host">
    <span class="label">主 催</span>
    <div class="org">みなと姿勢調整師会</div>
    <div class="addr">〒000-0000 みなと市中央区ひかり町1-2　TEL. 000-123-4567</div>
  </div>

  <section class="venue">
    <div class="venue-head">会 場</div>
    <div class="venue-name">ひかりプラザ <span>2階ホール</span></div>
    <div class="venue-addr">〒000-0000 みなと市中央区ひかり町3-4（駅前）</div>
    <div class="venue-map" role="img" aria-label="会場周辺の地図"></div>
  </section>

  <div class="contact"><span class="label">お問合せ先</span><span>担当：</span></div>
</main>
</body>
</html>
```